Business card for home decor store and design

I need a business card for my home decor boutique that’s professional looking boho/rustic. We sell vintage furniture, vintage finds, lamps, throws, rugs. We also carry a Diy paint line for refinishing furniture. We offer workshop on painting furniture, private or group setting. We in the heart of Old Town Red Bluff. We love to design, build and restore. Family owned small business. Our style is rustic boho farmhouse. We search for one of a kind found and repurposed items. We love vintage home decor, vintage windows.

Target Market(s)

Home decor

Industry/Entity Type

Home Accessories

Contact Information for Business Card

Have a rustic look/boho

Font styles to use
Serif
Script

Requirements
Must have
• Logo

```html
<!DOCTYPE html>
<html lang="en">
<head>
<meta charset="utf-8">
<title>Birch &amp; Loom Co. – Business Card</title>
<link rel="stylesheet" href="https://fonts.googleapis.com/css2?family=Oswald:wght@400;500;600&family=Lobster&display=swap">
<style>
  :root {
    --backdrop: #e8e8e8;
    --kraft-light: #e9cc9f;
    --kraft: #dcba88;
    --kraft-deep: #cfa874;
    --ink: #3d2a14;
    --banner-text: #d8b57f;
  }
  * { margin: 0; padding: 0; box-sizing: border-box; }
  html, body { width: 1200px; height: 960px; overflow: hidden; }
  body { background: var(--backdrop); position: relative; font-family: "Oswald", sans-serif; color: var(--ink); }

  .card { position: absolute; left: 311px; width: 579px; height: 330px; overflow: hidden; }
  .card--front { top: 130px; }
  .card--back { top: 512px; }

  .card__texture {
    position: absolute; inset: 0;
    background: radial-gradient(circle at 50% 50%, var(--kraft-light) 0%, var(--kraft) 55%, var(--kraft-deep) 100%);
  }
  .card--back .card__texture {
    background: radial-gradient(circle at 50% 45%, var(--kraft-light) 0%, var(--kraft) 55%, var(--kraft-deep) 100%);
  }

  .brand-mark { position: absolute; }
  .card--front .brand-mark { left: 164px; top: 55px; width: 220px; height: 220px; }
  .card--back .brand-mark { left: 79px; top: 38px; width: 160px; height: 160px; }
  .brand-mark svg { display: block; width: 100%; height: 100%; }
  .brand-mark__name { font-family: "Oswald", sans-serif; font-weight: 500; fill: var(--ink); }

  .flourish { position: absolute; left: 357px; width: 140px; height: 26px; background: var(--ink); opacity: .75; border-radius: 13px; }
  .flourish--top { top: 50px; }
  .flourish--bottom { top: 154px; }

  .person { position: absolute; left: 300px; width: 250px; text-align: center; }
  .person__name { top: 82px; font-family: "Lobster", cursive; font-size: 30px; line-height: 36px; }
  .person__role { top: 124px; font-size: 14px; font-weight: 500; letter-spacing: .5px; }

  .contact { position: absolute; }
  .contact__email { left: 300px; width: 250px; top: 199px; text-align: center; font-size: 14px; }
  .contact__rule { left: 34px; top: 230px; width: 512px; border-top: 2px dotted var(--ink); }
  .contact__divider { left: 290px; top: 234px; height: 32px; border-left: 2px dotted var(--ink); }
  .contact__address { left: 46px; top: 240px; font-size: 14px; line-height: 20px; }
  .contact__phone { left: 300px; width: 250px; top: 232px; text-align: center; font-size: 27px; font-weight: 600; line-height: 36px; }

  .web-banner { position: absolute; left: 34px; top: 271px; width: 512px; height: 32px; }
  .web-banner svg { position: absolute; inset: 0; }
  .web-banner__text { position: absolute; inset: 0; text-align: center; line-height: 32px; font-size: 19px; font-weight: 500; color: var(--banner-text); letter-spacing: .5px; }
</style>
</head>
<body>

<section class="card card--front">
  <div class="card__texture" role="img" aria-label="Kraft paper background with soft sunburst rays"></div>
  <div class="brand-mark">
    <svg viewBox="0 0 220 220">
      <circle cx="110" cy="110" r="104" fill="none" stroke="var(--ink)" stroke-width="6"/>
      <text class="brand-mark__name" x="110" y="120" text-anchor="middle" font-size="27">Birch &amp; Loom Co.</text>
    </svg>
  </div>
</section>

<section class="card card--back">
  <div class="card__texture" role="img" aria-label="Kraft paper background with soft sunburst rays"></div>
  <div class="brand-mark">
    <svg viewBox="0 0 160 160">
      <circle cx="80" cy="80" r="76" fill="none" stroke="var(--ink)" stroke-width="4.5"/>
      <text class="brand-mark__name" x="80" y="87" text-anchor="middle" font-size="20">Birch &amp; Loom Co.</text>
    </svg>
  </div>

  <div class="flourish flourish--top" role="img" aria-label="Decorative scroll ornament"></div>
  <h1 class="person person__name">Daniel Harper</h1>
  <p class="person person__role">OWNER</p>
  <div class="flourish flourish--bottom" role="img" aria-label="Decorative scroll ornament"></div>

  <p class="contact contact__email">daniel@birchandloomco.com</p>
  <div class="contact contact__rule"></div>
  <div class="contact contact__divider"></div>
  <p class="contact contact__address">412 Elm Street, Millbrook, CA 96000</p>
  <p class="contact contact__phone">530-555-0142</p>

  <div class="web-banner">
    <svg viewBox="0 0 512 32" preserveAspectRatio="none">
      <polygon points="0,0 512,0 500,16 512,32 0,32 12,16" fill="var(--ink)"/>
    </svg>
    <p class="web-banner__text">WWW.BIRCHANDLOOMCO.COM</p>
  </div>
</section>

</body>
</html>
```